Lumora business card for a plastic surgeon

we need a business card for plastic surgeons that work on a clinic called LUMORA.
we want a clean design and the following informations: name of the doctor, doctor's registration number (called CRM), telephone, address, facebook, instagram.
Colors: white, blue tones, light brown/ coffee

facebook and instagram: lumoracirurgiaestetica

Industry/Entity Type

Business

Contact Information for Business Card

clean design

Font styles to use
Serif
Sans Serif
Other font styles liked:
• helvetica light

Colors
cee9f5
85cae6
85abd2
3276b5
cfeae6
cedeed
eaf1f7

Requirements
Must have
• doctor's name
• identification number (called CRM)
• contact (phone, facebook, instagram, address)

```html
<!DOCTYPE html>
<html lang="pt">
<head>
<meta charset="utf-8">
<title>Lumora – Cartão de Visita</title>
<link href="https://fonts.googleapis.com/css2?family=Cinzel:wght@400&family=Open+Sans:wght@400&display=swap" rel="stylesheet">
<style>
  :root {
    --backdrop: #5f5d5e;
    --navy: #033358;
    --cyan: #00c0de;
    --white: #ffffff;
    --ink: #1e1e1e;
  }
  html, body {
    margin: 0;
    padding: 0;
    width: 992px;
    height: 1200px;
    overflow: hidden;
    background: var(--backdrop);
  }
  .canvas {
    position: relative;
    width: 992px;
    height: 1200px;
  }
  .card {
    position: absolute;
    overflow: hidden;
  }
  .card--front {
    left: 57px; top: 74px; width: 883px; height: 504px;
    background: var(--navy);
  }
  .card--back {
    left: 55px; top: 620px; width: 883px; height: 505px;
    background: var(--white);
  }
  .band { position: absolute; left: 0; width: 100%; }
  .band--cyan { background: var(--cyan); height: 12px; }
  .band--navy { background: var(--navy); }

  .wordmark {
    position: absolute;
    font-family: "Cinzel", Georgia, serif;
    font-weight: 400;
    color: var(--cyan);
    white-space: nowrap;
    line-height: 1;
    transform: translateX(-50%);
  }
  .card--front .wordmark { left: 50%; top: 188px; font-size: 62px; letter-spacing: 2px; }
  .card--back .wordmark  { left: 213px; top: 195px; font-size: 50px; letter-spacing: 2px; }

  .doctor {
    position: absolute;
    left: 497px;
    top: 100px;
    font-family: "Open Sans", Helvetica, Arial, sans-serif;
  }
  .doctor__name {
    margin: 0;
    font-size: 40px;
    font-weight: 400;
    color: var(--cyan);
    line-height: 1;
    letter-spacing: 0.5px;
  }
  .doctor__crm {
    margin: 12px 0 0;
    font-size: 22px;
    color: var(--navy);
    line-height: 1;
  }
  .doctor__rule {
    position: absolute;
    left: 495px; top: 181px;
    width: 388px; height: 1px;
    background: var(--cyan);
  }
  .contacts {
    position: absolute;
    left: 495px;
    top: 216px;
    margin: 0; padding: 0;
    list-style: none;
    font-family: "Open Sans", Helvetica, Arial, sans-serif;
    font-size: 19px;
    line-height: 24px;
    color: var(--ink);
  }
  .contact {
    display: flex;
    align-items: center;
    gap: 6px;
    margin-bottom: 14px;
  }
  .contact__icon { width: 35px; height: 37px; flex: none; }
</style>
</head>
<body>
<div class="canvas">

  <section class="card card--front">
    <div class="band band--cyan" style="top:25px"></div>
    <div class="band band--cyan" style="top:469px"></div>
    <div class="wordmark">LUMORA</div>
  </section>

  <section class="card card--back">
    <div class="band band--navy" style="top:0;height:25px"></div>
    <div class="band band--cyan" style="top:25px"></div>
    <div class="band band--cyan" style="top:468px"></div>
    <div class="band band--navy" style="top:480px;height:25px"></div>

    <div class="wordmark">LUMORA</div>

    <div class="doctor">
      <h1 class="doctor__name">NAME HERE</h1>
      <p class="doctor__crm">CRM 121212</p>
    </div>
    <div class="doctor__rule"></div>

    <ul class="contacts">
      <li class="contact">
        <svg class="contact__icon" viewBox="0 0 35 37" aria-hidden="true">
          <rect x="0" y="1" width="35" height="35" rx="6" fill="var(--cyan)"/>
          <path d="M17.5 7a8 8 0 0 0-8 8c0 6 8 14 8 14s8-8 8-14a8 8 0 0 0-8-8z" fill="#fff"/>
          <circle cx="17.5" cy="15" r="3.2" fill="var(--cyan)"/>
        </svg>
        <span>8630 abcdeford Rd. Suite 154<br>your city, mnopqurs 21046</span>
      </li>
      <li class="contact">
        <svg class="contact__icon" viewBox="0 0 35 37" aria-hidden="true">
          <rect x="0" y="1" width="35" height="35" rx="6" fill="var(--cyan)"/>
          <rect x="5" y="5" width="25" height="27" rx="5" fill="#fff"/>
          <path d="M12 10c-2 1-3 3-2 6 1 4 5 9 9 11 3 1 5 0 6-2l-3-3-2 1c-2-1-4-4-5-6l1-2z" fill="var(--cyan)"/>
        </svg>
        <span>000.1234.5678<br>000.1234.2564</span>
      </li>
      <li class="contact">
        <svg class="contact__icon" viewBox="0 0 35 37" aria-hidden="true">
          <rect x="0" y="1" width="35" height="35" rx="6" fill="var(--cyan)"/>
          <circle cx="17.5" cy="18.5" r="12" fill="none" stroke="#fff" stroke-width="2"/>
          <ellipse cx="17.5" cy="18.5" rx="5" ry="12" fill="none" stroke="#fff" stroke-width="1.5"/>
          <rect x="5" y="14.5" width="25" height="8" fill="#fff"/>
          <text x="17.5" y="21" text-anchor="middle" font-family="Open Sans, Arial, sans-serif" font-size="6.5" fill="var(--cyan)">www</text>
        </svg>
        <span>lumoracirurgiaestetica<br>lumoracirurgiaestetica</span>
      </li>
    </ul>
  </section>

</div>
</body>
</html>
```